Website for small historic hotel called the Harrow Crest

We are looking to design a website for a small Inn/Hotel.
Site would need to be able to take reservations and flow through to booking via Tillpoint with orbit pay, vantor pay and lumichat pay (Chinese verson )
We would have links from Verano, Jauntly.com, roam scout etc to our website for booking purposes
Here are some examples of small inn/hotels doing the same sort of thing in our area. Provided purely for reference, not to be plagiarized!
https://innvelmoor.com/caddicks/
https://www.pellowgate.ca/hotel
https://www.duchessinnvelmoor.ca/hotel
https://www.thekellaway.ca/
We will also provide you some photos, once the site has been done, to utilize instead of random shots taken from the internet as placeholders
I have also provided a link to some hotels in Perthshire Scotland which may also provide you with some ideas Again please do not plagiarise
https://drumvaillhouse.com/
https://www.theinnatlochcarvey.com/
https://www.brenmorarmshotel.com/
http://www.highland-lodgings.co.uk/NorthvaleandCardross.htm
Our inn is in Perth County in Ontario Canada NOT Scotland but the original owner was a Dalgairn from Perthshire Scotland and is responsible for the county being named Perth
We would need a landing page plus the following
page for rooms
Page for booking
Contact page
About US Page
Total site is landing page plus 4 or 5 sub pages
The general outline is provided. Please contact me with specific questions
Just as an update the folllowing are the placeholder names for the pages. They will be tabs at the top right and fllow through to sub pages off the main landing page
MAIN LANDING PAGE links at top to
1 _ history - the story of the building and Dalgairn
2_ Contact
3_ Rooms and Suites - will have each room and suite and link to sub-page for each
4 _ Perth County
5 - to be determined
The following would be sub pages
3 will display links to the suites: with a sub-page for each suite
Garden Suite - includes a 500 square foot patio and garden
Reception Suite - under renovation
Parlour Suite - Old parlor - Under renovation
GLASBURNIE Suite - Under renovation
1854 Suite 0- Under renovation
Updates
Just some additional information
The Inn/Hotel this website is for is named after a native of Perthshire Scotland who is also responsible for the area being names Perth County
The building is constructed in the 1850's and the decor and design are those of small-town inns you can find in the British Isles - England, Scotonal, Ireland and Wales
Some examples from Perthshire in Scotland - for inspiration, not plagiarisation!
https://drumvaillhouse.com/
Please note the inn does not have a restaurant at present and only offers rooms
Feel free to submitt any questions for clarification
I have also provided a link to some hotels in Perthshire Scotland with similar designs and crests as well as to give you some background as to Perth. Again please do not plagiarise
https://drumvaillhouse.com/
This is provided as an outline and we can answer specific questions
Few if any designs of any quality were received. Really nowhere near what was promised and certainly not the quality or quantity I would expect RT, whom I worked with before and I invited, submitted the bulk of the entries
Industry/Entity Type
boutique hotel - 19th century traditional British Isles
Number of Pages Required
5+ page
Look and feel
Each slider illustrates characteristics of the customer's brand and the style your logo design should communicate.

```html
<!DOCTYPE html>
<html lang="en">
<head>
<meta charset="utf-8">
<title>Harrow Crest Hotel, Perth County</title>
<link rel="stylesheet" href="https://fonts.googleapis.com/css2?family=Cormorant+Garamond:wght@500;600&family=Libre+Baskerville:wght@400;700&family=Outfit:wght@300;400;500;600&family=Inter:wght@600&display=swap">
<style>
:root{
  --navy:#1e3784;
  --navy-deep:#1b3380;
  --gold:#d9a43c;
  --white:#ffffff;
  --card:#f6f6f8;
  --muted:#5a6fb3;
  --rule:#3a52a0;
}
*{margin:0;padding:0;box-sizing:border-box}
html,body{width:1200px;height:3136px;overflow:hidden;background:var(--white)}
body{position:relative;font-family:"Outfit",sans-serif;color:var(--navy)}
.abs{position:absolute}
.logo{font-family:"Inter",sans-serif;font-weight:600;font-size:23px;letter-spacing:-.3px}
.header-logo{left:74px;top:38px;color:var(--navy)}
.nav{position:absolute;top:48px;left:362px;display:flex;gap:28px;font-family:"Libre Baskerville",serif;font-size:14px;white-space:nowrap}
.nav a{color:var(--navy);text-decoration:none}
.nav a.active{color:var(--gold)}
.book-btn{left:965px;top:34px;width:160px;height:47px;background:var(--navy);color:#fff;font-family:"Libre Baskerville",serif;font-weight:700;font-size:16px;display:flex;align-items:center;justify-content:center}
.photo{position:absolute}
.hero{left:0;top:107px;width:1200px;height:469px;background:linear-gradient(160deg,#a66a43 0%,#8c6a3d 35%,#c9a55a 55%,#8a7a62 75%,#5e6a3a 100%)}
.booking{left:74px;top:501px;width:1051px;height:149px;background:var(--navy)}
.field-label{position:absolute;top:31px;color:#fff;font-size:14px;font-weight:500;letter-spacing:3px}
.field{position:absolute;top:66px;height:55px;background:#fff;font-family:"Libre Baskerville",serif;font-size:24px;color:var(--navy);display:flex;align-items:center;padding-left:19px}
.field svg{position:absolute;right:34px;top:18px}
.check-btn{position:absolute;left:867px;top:66px;width:154px;height:55px;background:var(--gold);color:#fff;font-size:14px;font-weight:500;letter-spacing:3px;display:flex;align-items:center;justify-content:center}
.serif-head{font-family:"Cormorant Garamond",serif;font-weight:500;color:var(--navy)}
.welcome-title{left:68px;top:740px;font-size:40px}
.welcome-text{left:74px;top:834px;width:590px;font-size:18.5px;line-height:23.5px;font-weight:300}
.welcome-text p+p{margin-top:23.5px}
.castle{left:698px;top:834px;width:338px;height:233px;background:linear-gradient(180deg,#9da3a8 0%,#c5c7c4 40%,#5f7a3c 70%,#3c5a25 100%)}
.feature{position:absolute;top:1245px;width:338px}
.feature .img{height:234px}
.feature h3{margin-top:17px;text-align:center;font-family:"Cormorant Garamond",serif;font-weight:500;font-size:30px}
.banner{left:0;top:1624px;width:1200px;height:468px;background:linear-gradient(180deg,#5b5e60 0%,#4a513f 40%,#3b4a26 70%,#2c351c 100%)}
.banner-title{left:0;top:1805px;width:1200px;text-align:center;font-size:61px;color:#fff}
.banner-sub{left:0;top:1882px;width:1200px;text-align:center;font-size:18px;font-weight:300;color:#fff}
.reviews-title{left:0;top:2132px;width:1200px;text-align:center;font-size:62px}
.reviews-sub{left:0;top:2206px;width:1200px;text-align:center;font-size:21px;font-weight:300}
.review{position:absolute;top:2326px;width:337px;height:287px;background:var(--card);padding:19px}
.avatar{position:absolute;left:19px;top:19px;width:74px;height:74px;border-radius:50%;background:radial-gradient(circle,#c9a085 0%,#7e6a5c 70%,#4a3f39 100%)}
.reviewer{position:absolute;left:108px;top:34px;font-family:"Libre Baskerville",serif;font-weight:700;font-size:19px}
.stars{position:absolute;left:108px;top:60px;display:flex;gap:2px}
.review-text{position:absolute;left:19px;top:113px;width:300px;font-size:16px;line-height:25.5px;font-weight:300}
.arrow{position:absolute;top:2457px}
.newsletter-band{left:0;top:2766px;width:1200px;height:370px;background:var(--navy-deep)}
.newsletter{left:253px;top:2708px;width:694px;height:103px;background:var(--gold)}
.newsletter h2{position:absolute;left:28px;top:16px;font-family:"Cormorant Garamond",serif;font-weight:500;font-size:38px;line-height:34px;color:#fff}
.newsletter .email{position:absolute;left:337px;top:30px;width:207px;height:45px;background:#fff;border-radius:3px;font-size:15px;color:var(--navy-deep);padding:15px 14px}
.newsletter .submit{position:absolute;left:553px;top:30px;width:113px;height:45px;background:var(--navy-deep);border-radius:3px;color:#fff;font-size:16px;font-weight:500;display:flex;align-items:center;justify-content:center}
.footer-logo{left:74px;top:2860px;color:var(--gold)}
.footer-head{font-size:14px;font-weight:600;color:#fff}
.footer-col{position:absolute;top:2859px}
.footer-col ul{list-style:none;margin-top:9px}
.footer-col li{font-size:14px;color:var(--muted);line-height:32px;font-weight:300}
.address{left:74px;top:2913px}
.address p{font-size:14px;color:var(--muted);line-height:30px;font-weight:300;margin-top:6px}
.footer-rule{left:74px;top:3068px;width:1051px;height:1px;background:var(--rule)}
.copyright{left:74px;top:3096px;font-size:11px;color:var(--muted);font-weight:300}
</style>
</head>
<body>
<header>
  <div class="abs logo header-logo">Harrow Crest</div>
  <nav class="nav">
    <a class="active" href="#">Home</a><a href="#">About</a><a href="#">Rooms</a><a href="#">Activities</a><a href="#">Offter &amp; Packages</a><a href="#">Contact</a>
  </nav>
  <div class="abs book-btn">Book A Room</div>
</header>

<div class="photo hero" role="img" aria-label="Historic sandstone buildings with autumn trees"></div>

<section class="abs booking">
  <div class="field-label" style="left:29px">ARRIVE</div>
  <div class="field-label" style="left:335px">DEPARTURE</div>
  <div class="field-label" style="left:640px">ADULTS</div>
  <div class="field-label" style="left:754px">CHILDREN</div>
  <div class="field" style="left:29px;width:286px">14/5/2022
    <svg width="22" height="20" viewBox="0 0 22 20"><rect x="1" y="3" width="20" height="16" rx="2" fill="none" stroke="#d9a43c" stroke-width="1.6"/><rect x="1" y="3" width="20" height="4" fill="#d9a43c"/><g fill="#d9a43c"><rect x="4" y="9" width="3" height="2"/><rect x="9" y="9" width="3" height="2"/><rect x="14" y="9" width="3" height="2"/><rect x="4" y="13" width="3" height="2"/><rect x="9" y="13" width="3" height="2"/><rect x="14" y="13" width="3" height="2"/></g></svg>
  </div>
  <div class="field" style="left:335px;width:286px">16/5/2022
    <svg width="22" height="20" viewBox="0 0 22 20"><rect x="1" y="3" width="20" height="16" rx="2" fill="none" stroke="#d9a43c" stroke-width="1.6"/><rect x="1" y="3" width="20" height="4" fill="#d9a43c"/><g fill="#d9a43c"><rect x="4" y="9" width="3" height="2"/><rect x="9" y="9" width="3" height="2"/><rect x="14" y="9" width="3" height="2"/><rect x="4" y="13" width="3" height="2"/><rect x="9" y="13" width="3" height="2"/><rect x="14" y="13" width="3" height="2"/></g></svg>
  </div>
  <div class="field" style="left:640px;width:93px">2</div>
  <div class="field" style="left:755px;width:93px">1</div>
  <div class="check-btn">CHECK</div>
</section>

<h1 class="abs serif-head welcome-title">Welcome to Harrow Crest Hotel, Perth County</h1>
<div class="abs welcome-text">
  <p>Lorem ipsum dolor sit amet, consectetur adipiscing elit, sed do eiusmod tempor incididunt ut labore et dolore magna aliqua. Ut enim ad minim veniam, quis nostrud exercitation ullamco laboris nisi ut aliquip ex ea commodo consequat. Duis aute irure dolor in reprehenderit in voluptate velit esse cillum dolore eu fugiat nulla pariatur. Excepteur sint occaecat cupidatat non proident, sunt in culpa qui officia deserunt mollit anim id est laborum.</p>
  <p>Sed ut perspiciatis unde omnis iste natus error sit voluptatem accusantium doloremque laudantium, totam rem aperiam, eaque ipsa quae ab illo inventore veritatis et quasi architecto beatae vitae dicta sunt explicabo. Nemo enim ipsam voluptatem quia voluptas sit aspernatur</p>
</div>
<div class="photo castle" role="img" aria-label="Castle with formal gardens under a cloudy sky"></div>

<section>
  <div class="feature" style="left:74px"><div class="img" role="img" aria-label="Guest room with timber ceiling and twin beds" style="background:linear-gradient(180deg,#6b4526 0%,#8a7462 45%,#b9ae9f 75%,#8f8c99 100%)"></div><h3>Our Rooms</h3></div>
  <div class="feature" style="left:431px"><div class="img" role="img" aria-label="Stone castle on a misty loch" style="background:linear-gradient(180deg,#c5c9c4 0%,#7b8870 45%,#3e4d2e 65%,#7f8b87 100%)"></div><h3>Amenities</h3></div>
  <div class="feature" style="left:787px"><div class="img" role="img" aria-label="Stone bridge leading to a castle" style="background:linear-gradient(180deg,#3f7a9c 0%,#6a9fba 25%,#3f6b33 55%,#8c8c86 100%)"></div><h3>City &amp; Culture</h3></div>
</section>

<div class="photo banner" role="img" aria-label="Rugged green highland landscape under grey clouds"></div>
<h2 class="abs serif-head banner-title" style="color:#fff">Amazing Perth County</h2>
<p class="abs banner-sub">Lorem ipsum dolor sit amet, consectetur</p>

<h2 class="abs serif-head reviews-title">Reviews</h2>
<p class="abs reviews-sub">Lorem ipsum dolor sit amet, consectetur</p>

<svg class="arrow" style="left:26px" width="16" height="26" viewBox="0 0 16 26"><path d="M13 2 3 13l10 11" fill="none" stroke="#d9a43c" stroke-width="2"/></svg>
<svg class="arrow" style="left:1156px" width="16" height="26" viewBox="0 0 16 26"><path d="M3 2l10 11L3 24" fill="none" stroke="#d9a43c" stroke-width="2"/></svg>

<section>
  <article class="review" style="left:74px">
    <div class="avatar" role="img" aria-label="Reviewer portrait"></div>
    <div class="reviewer">Ewan Tallisker</div>
    <div class="stars"><svg width="96" height="16" viewBox="0 0 96 16"><g fill="#d9a43c"><path id="s" d="M8 0l2.4 5 5.4.6-4 3.7 1.1 5.4L8 12 3.1 14.7l1.1-5.4-4-3.7 5.4-.6z"/><use href="#s" x="19"/><use href="#s" x="38"/><use href="#s" x="57"/><use href="#s" x="76"/></g></svg></div>
    <p class="review-text">Lorem ipsum dolor sit amet, consectetur adipiscing elit, sed do eiusmod tempor incididunt ut labore et dolore magna aliqua. Ut enim ad minim veniam, quis nostrud exercitation ullamco laboris nisi ut aliquip ex ea commodo consequat.</p>
  </article>
  <article class="review" style="left:433px">
    <div class="avatar" role="img" aria-label="Reviewer portrait"></div>
    <div class="reviewer">Marigold88</div>
    <div class="stars"><svg width="96" height="16" viewBox="0 0 96 16"><g fill="#d9a43c"><use href="#s"/><use href="#s" x="19"/><use href="#s" x="38"/><use href="#s" x="57"/><use href="#s" x="76"/></g></svg></div>
    <p class="review-text">Lorem ipsum dolor sit amet, consectetur adipiscing elit, sed do eiusmod tempor incididunt ut labore et dolore magna aliqua. Ut enim ad minim veniam, quis nostrud exercitation ullamco laboris nisi ut aliquip ex ea commodo consequat.</p>
  </article>
  <article class="review" style="left:791px">
    <div class="avatar" role="img" aria-label="Reviewer portrait"></div>
    <div class="reviewer">Corrie41</div>
    <div class="stars"><svg width="96" height="16" viewBox="0 0 96 16"><g fill="#d9a43c"><use href="#s"/><use href="#s" x="19"/><use href="#s" x="38"/><use href="#s" x="57"/><use href="#s" x="76"/></g></svg></div>
    <p class="review-text">Lorem ipsum dolor sit amet, consectetur adipiscing elit, sed do eiusmod tempor incididunt ut labore et dolore magna aliqua. Ut enim ad minim veniam, quis nostrud exercitation ullamco laboris nisi ut aliquip ex ea commodo consequat.</p>
  </article>
</section>

<footer>
  <div class="abs newsletter-band"></div>
  <div class="abs newsletter">
    <h2>Subscribe To<br>Newsletter</h2>
    <div class="email">Email</div>
    <div class="submit">Submit</div>
  </div>
  <div class="abs logo footer-logo">Harrow Crest</div>
  <div class="abs address">
    <div class="footer-head">Address</div>
    <p>Harrow Crest, 418 Aldergate Rd,<br>Suite 12 Brookvale, ON N0K 3R7</p>
  </div>
  <div class="footer-col" style="left:453px"><div class="footer-head">Get Started</div><ul><li>Enterprise</li><li>Retail</li><li>Professional Services</li><li>Field Services</li><li>Healthcare</li></ul></div>
  <div class="footer-col" style="left:707px"><div class="footer-head">Navigation</div><ul><li>Home</li><li>Features</li><li>Pricing</li><li>FAQ</li><li>Contact</li></ul></div>
  <div class="footer-col" style="left:871px"><div class="footer-head">Social</div><ul><li>Snapwell</li><li>Friendhall</li><li>Reelcast</li></ul></div>
  <div class="footer-col" style="left:1031px"><div class="footer-head">Our Policies</div><ul><li>Privacy Policy</li><li>Terms of Use</li></ul></div>
  <div class="abs footer-rule"></div>
  <div class="abs copyright">© 2022 Harrow Crest. All Rights Reserved</div>
</footer>
</body>
</html>
```